Marlow Hire Business Card for recruitment company

We are looking for a Business Card Design that incorporates our personal details and our busines name and logo. We are a specialized search consultancy that recruit Property and Construction professionals.
We would like a business card that stands out and is appealing to the Construction and Property industry as well.

Target Market(s)

people in the construction and property industry

Contact Information for Business Card

Business Name and logo

Font styles to use
Serif

Colors
0094D4
00A9DD
6FCCEA
C7EBF8
E9F6FB

Requirements
Must have
• Business name and logo as well as contact details
Should not have
• No photos of us please

```html
<!DOCTYPE html>
<html lang="en">
<head>
<meta charset="utf-8">
<title>Marlow Hire — Business Card</title>
<link rel="stylesheet" href="https://fonts.googleapis.com/css2?family=Source+Sans+3:wght@300;400;600;700&display=swap">
<style>
  :root {
    --backdrop: #ebebeb;
    --card-white: #f3f3f5;
    --ink: #0c3346;
    --ink-soft: #2c3a44;
    --teal-light: #064a63;
    --teal-dark: #012737;
    --logo-white: #f4f6f7;
  }
  * { margin: 0; padding: 0; box-sizing: border-box; }
  html, body {
    width: 1200px; height: 1200px; overflow: hidden;
    background: var(--backdrop);
    font-family: "Source Sans 3", sans-serif;
  }
  .canvas { position: relative; width: 1200px; height: 1200px; }

  .card {
    position: absolute; left: 263px; width: 682px; height: 390px;
    border-radius: 36px; overflow: hidden;
  }
  .card--front { top: 165px; }
  .card--back { top: 654px; background: var(--card-white); }

  .front-pattern {
    position: absolute; inset: 0;
    background: linear-gradient(90deg, var(--teal-light) 0%, #04405a 40%, var(--teal-dark) 100%);
  }
  .front-brand {
    position: absolute; left: 82px; top: 280px;
    display: flex; align-items: center; gap: 10px;
    color: var(--logo-white); font-weight: 600; font-size: 24px; letter-spacing: 0.5px;
  }
  .front-brand .dot {
    width: 14px; height: 14px; border-radius: 50%; background: var(--logo-white);
  }

  .identity {
    position: absolute; left: 67px; top: 78px;
    border-left: 6px solid var(--ink); padding-left: 14px;
  }
  .identity .name { color: var(--ink); font-weight: 700; font-size: 21px; line-height: 1.15; }
  .identity .role { color: var(--ink-soft); font-weight: 400; font-size: 15.5px; line-height: 1.3; }

  .wordmark {
    position: absolute; left: 327px; top: 172px;
    color: var(--ink); font-weight: 400; font-size: 41px; letter-spacing: 1.5px;
    text-transform: uppercase; line-height: 1;
  }

  .contacts { position: absolute; left: 64px; top: 255px; list-style: none; }
  .contacts li {
    display: flex; align-items: center; gap: 10px;
    color: var(--ink-soft); font-weight: 300; font-size: 15.5px; line-height: 20px;
  }
  .contacts svg { width: 13px; height: 13px; fill: none; stroke: var(--ink); stroke-width: 1.6; }
</style>
</head>
<body>
<div class="canvas">
  <section class="card card--front">
    <div class="front-pattern" role="img" aria-label="Repeating pattern of the Marlow Hire emblem on a deep teal ground"></div>
    <div class="front-brand"><span class="dot"></span>Marlow Hire</div>
  </section>

  <section class="card card--back">
    <div class="identity">
      <p class="name">Hannah Ellery</p>
      <p class="role">Director</p>
      <p class="role">Senior Search Consultant</p>
    </div>

    <p class="wordmark">Marlow Hire</p>

    <ul class="contacts">
      <li>
        <svg viewBox="0 0 14 14"><path d="M3 1.5l2 2.5-1.2 1.3a7 7 0 0 0 4.9 4.9L10 9l2.5 2-1.3 1.8C6 12.5 1.5 8 1.2 2.8z"/></svg>
        +64 27 480 2291
      </li>
      <li>
        <svg viewBox="0 0 14 14"><rect x="1" y="3" width="12" height="8"/><path d="M1 3l6 5 6-5"/></svg>
        hannah@marlowhire.nz
      </li>
      <li>
        <svg viewBox="0 0 14 14"><circle cx="7" cy="7" r="5.8"/><ellipse cx="7" cy="7" rx="2.5" ry="5.8"/><path d="M1.2 7h11.6"/></svg>
        www.marlowhire.nz
      </li>
    </ul>
  </section>
</div>
</body>
</html>
```